WEBSITE NEEDED FOR MY COMPANY CALLED BRAVERIDGE HOCKEY DEVELOPMENT

LOOKING FOR A WEBSITE TO MARKET AND SEEL MY HOCKEY DEVELOPMENT PROGRAMS.
NEEDS TO HAVE 5+ PAGES

Target Market(s)

YOUTH SPORTS

Industry/Entity Type

YOUTH ATHLETE DEVELOPMENT

Number of Pages Required

5+ page

Font styles to use
Sans Serif

Colors
0054AA
0677BA
7BADD7
CADEEF
E8F1F8

Requirements
Must have
• MAIN PAGE - SPIRNG PROGRAM PAGE - SUMMER PROGRAM PAGE - WINTER PAGE - TOURNAMENT PAGE
Nice to have
• FLASH
Should not have
• NOT SURE

```html
<!DOCTYPE html>
<html lang="en">
<head>
<meta charset="utf-8">
<title>Braveridge Hockey Development</title>
<link href="https://fonts.googleapis.com/css2?family=Exo+2:wght@300;400;600;700;800&family=Montserrat:wght@400;500;600;700&display=swap" rel="stylesheet">
<style>
:root{
  --navy:#0a44a3;
  --royal:#0054aa;
  --sky:#2aaee5;
  --mid:#0677ba;
  --soft:#7badd7;
  --pale:#e8f1f8;
  --pale-2:#eef5fc;
  --ink:#1b1b1b;
  --white:#ffffff;
}
*{margin:0;padding:0;box-sizing:border-box}
html,body{width:1200px;height:3438px;overflow:hidden}
body{position:relative;background:var(--white);font-family:"Montserrat",sans-serif;color:var(--ink)}
a{text-decoration:none}
.abs{position:absolute}

/* brand */
.brand{position:absolute;font-family:"Exo 2",sans-serif;font-weight:800;font-size:21px;line-height:24px;color:var(--sky);letter-spacing:.5px;display:flex;align-items:center;gap:8px;white-space:nowrap}
.brand .dot{width:12px;height:12px;background:var(--sky);display:inline-block;flex:none}

/* nav */
.nav{position:absolute;top:32px;left:0;width:1200px;height:20px}
.nav a{position:absolute;color:var(--white);font-weight:600;font-size:13px;letter-spacing:.5px;white-space:nowrap}
.nav .home-mark{position:absolute;left:381px;top:-12px}

/* hero */
.hero{position:absolute;left:0;top:0;width:1200px;height:728px;
  background:radial-gradient(ellipse at 68% 38%, #4b5a6c 0%, #1c2c3f 40%, #0c1622 75%),#0c1622}
.hero-photo{position:absolute;left:0;top:0;width:1200px;height:728px;
  background:linear-gradient(180deg,rgba(0,0,0,0) 55%,rgba(120,140,160,.55) 85%,rgba(160,175,190,.7) 100%)}
.hero .kicker{position:absolute;left:108px;top:268px;color:var(--white);font-family:"Exo 2",sans-serif;font-weight:300;font-size:25px;letter-spacing:5px}
.hero h1{position:absolute;left:106px;top:302px;color:var(--white);font-family:"Exo 2",sans-serif;font-weight:800;font-size:54px;line-height:62px;letter-spacing:.5px}
.btn{display:flex;align-items:center;justify-content:center;border-radius:40px;font-weight:700;text-transform:uppercase;color:var(--white);background:var(--sky)}
.hero .btn{position:absolute;left:109px;top:442px;width:190px;height:48px;font-size:14px;letter-spacing:.5px}
.slide-dots span{position:absolute;left:1154px;width:10px;height:10px;border-radius:50%;background:var(--white)}
.slide-dots span.off{background:none;border:1.5px solid var(--white)}

/* section headings */
.sec-title{position:absolute;left:0;width:1200px;text-align:center;font-family:"Exo 2",sans-serif;font-size:38px;font-weight:300;color:var(--ink)}
.sec-title b{font-weight:700}
.rule{position:absolute;height:3px;background:var(--sky)}

/* spring cards */
.card-photo{position:absolute;width:334px;height:249px}
.card-box{position:absolute;width:284px;height:155px;background:var(--white);box-shadow:0 4px 14px rgba(0,0,0,.12);text-align:center}
.card-box h3{margin-top:33px;font-family:"Exo 2",sans-serif;font-weight:700;font-size:17px;color:var(--sky)}
.card-box p{margin-top:2px;font-size:13px;line-height:19px;color:var(--ink)}
.card-box .btn{width:116px;height:29px;margin:14px auto 0;font-size:8.5px;letter-spacing:.3px}
.card-box.featured{background:var(--navy)}
.card-box.featured h3,.card-box.featured p{color:var(--white)}
.pager span{position:absolute;top:1256px;height:4px;width:49px;border-radius:2px;background:#a8d6f0}
.pager span.on{background:var(--mid)}

/* winter */
.winter{position:absolute;left:0;top:1338px;width:1200px;height:595px;
  background:radial-gradient(circle at 36% 45%, #6f9dc5 0%, #2f5f8f 35%, #142d4a 75%)}
.winter h2{position:absolute;left:681px;top:150px;font-family:"Exo 2",sans-serif;font-weight:700;font-size:43px;color:var(--white)}
.winter .rule{left:681px;top:205px;width:67px;background:var(--white)}
.winter p{position:absolute;left:682px;width:470px;color:var(--white);font-size:15.5px;line-height:23.5px}
.btn-outline{position:absolute;left:686px;top:419px;width:178px;height:47px;border:2px solid var(--white);border-radius:30px;color:var(--white);font-weight:600;font-size:14.5px;letter-spacing:.5px;display:flex;align-items:center;justify-content:center}

/* tournaments */
.featured-bg{position:absolute;left:0;top:1933px;width:1200px;height:681px;background:var(--pale-2)}
.t-card{position:absolute;top:2199px;width:301px;height:291px;border:1.5px solid var(--soft);text-align:center}
.t-card h3{margin-top:155px;font-family:"Exo 2",sans-serif;font-weight:700;font-size:19px;color:var(--sky)}
.t-card p{font-size:13px;line-height:19px;margin-top:1px}
.t-card .btn{width:123px;height:29px;margin:10px auto 0;font-size:9px}
.t-photo{position:absolute;width:240px;height:240px;border-radius:50%}

/* summer */
.summer-photo{position:absolute;left:395px;top:2673px;width:713px;height:500px;
  background:linear-gradient(180deg,#3a2c22 0%,#7a6046 45%,#b7a994 75%,#dad6d2 100%)}
.summer h2{position:absolute;left:156px;top:2797px;font-family:"Exo 2",sans-serif;font-weight:400;font-size:34px;color:var(--ink)}
.summer h2 b{font-weight:700}
.summer p{position:absolute;left:156px;top:2858px;width:400px;font-size:16.5px;line-height:23.5px;color:#3a3a3a;white-space:nowrap}
.summer .btn{position:absolute;left:152px;top:2997px;width:171px;height:44px;background:var(--navy);font-size:14px}

/* footer */
.footer-links a{position:absolute;top:3320px;color:var(--white);font-weight:700;font-size:12px;white-space:nowrap}
.copyright{position:absolute;left:311px;top:3349px;color:var(--white);font-size:11.5px}
.social span{position:absolute;top:3315px;width:24px;height:24px;border-radius:50%;border:1.5px solid var(--white)}
</style>
</head>
<body>

<!-- HERO -->
<section class="hero">
  <div class="hero-photo" role="img" aria-label="Two hockey players battling for the puck on an indoor rink"></div>
  <p class="kicker">HOCKEY TOURNAMENT</p>
  <h1>BRAVERIDGE HOCKEY<br>DEVELOPMENT</h1>
  <a class="btn" href="#">View Program</a>
  <div class="slide-dots">
    <span style="top:325px"></span><span style="top:347px"></span><span style="top:369px"></span><span class="off" style="top:390px"></span>
  </div>
  <svg class="abs" style="left:0;top:640px" width="1200" height="90" viewBox="0 0 1200 90">
    <path d="M0 90 C300 10 800 0 1200 80 L1200 90 Z" fill="#ffffff"/>
    <path d="M40 88 C400 12 820 0 1200 52 L1200 84 C860 18 420 22 40 88 Z" fill="#0a44a3"/>
  </svg>
</section>

<header>
  <div class="brand" style="left:120px;top:30px"><span class="dot"></span>BRAVERIDGE</div>
  <nav class="nav">
    <a href="#" style="left:339px">HOME</a>
    <svg class="home-mark" width="22" height="40" viewBox="0 0 22 40"><path d="M20 2 L6 34 L1 36" stroke="#2aaee5" stroke-width="2.5" fill="none" stroke-linecap="round"/></svg>
    <a href="#" style="left:450px">SPRING PROGRAM</a>
    <a href="#" style="left:643px">SUMMER PROGRAM</a>
    <a href="#" style="left:844px">WINTER</a>
    <a href="#" style="left:973px">TOURNAMENT</a>
  </nav>
</header>

<!-- SPRING PROGRAMS -->
<h2 class="sec-title" style="top:755px">SPRING <b>PROGRAMS</b></h2>
<div class="rule" style="left:549px;top:806px;width:94px"></div>

<div class="card-photo" style="left:88px;top:856px;background:radial-gradient(circle at 50% 20%,#d7e6f5 0%,#6d8bb0 35%,#243854 75%)" role="img" aria-label="Youth players skating under arena lights"></div>
<div class="card-photo" style="left:440px;top:856px;background:radial-gradient(circle at 50% 25%,#c9cfd6 0%,#4a5563 40%,#151b23 80%)" role="img" aria-label="Player handling the puck in a dark arena"></div>
<div class="card-photo" style="left:792px;top:856px;background:linear-gradient(180deg,#1b2440 0%,#3a4a6d 45%,#d6e2ea 75%,#eef3f6 100%)" role="img" aria-label="Empty hockey arena with ice surface"></div>

<div class="card-box" style="left:115px;top:1049px"><h3>SPRING PROGRAM TITLE</h3><p>Lorem ipsum dolor sit amet<br>consectetur adipiscing</p><a class="btn" href="#">View Program</a></div>
<div class="card-box featured" style="left:466px;top:1049px"><h3>SPRING PROGRAM TITLE</h3><p>Lorem ipsum dolor sit amet<br>consectetur adipiscing</p><a class="btn" href="#">View Program</a></div>
<div class="card-box" style="left:817px;top:1049px"><h3>SPRING PROGRAM TITLE</h3><p>Lorem ipsum dolor sit amet<br>consectetur adipiscing</p><a class="btn" href="#">View Program</a></div>

<div class="pager"><span class="on" style="left:525px"></span><span style="left:580px"></span><span style="left:635px"></span></div>

<!-- WINTER -->
<section class="winter" role="img" aria-label="Hockey puck flying toward the camera with a player spraying ice behind">
  <svg class="abs" style="left:0;top:0" width="1200" height="595" viewBox="0 0 1200 595">
    <defs><linearGradient id="winterBlue" x1="0" y1="0" x2="1" y2="0"><stop offset="0" stop-color="#1b6fc0" stop-opacity=".92"/><stop offset="1" stop-color="#1a86d2"/></linearGradient></defs>
    <path d="M788 0 C600 120 540 400 700 595 L1200 595 L1200 0 Z" fill="url(#winterBlue)"/>
  </svg>
  <h2>WINTER HOCKEY</h2>
  <div class="rule"></div>
  <p style="top:227px">Lorem ipsum dolor sit amet, consectetur adipiscing elit, sed<br>do eiusmod tempor incididunt ut labore et</p>
  <p style="top:298px">aliqua. Ut enim ad minim veniam, quis nostrud exercitation<br>ullamco laboris nisi ut aliquip ex ea commodo consequat.<br>Duis aute irure dolor in reprehenderit in voluptate velit esse<br>cillum dolore eu fugiat nulla pariatur.</p>
  <a class="btn-outline" href="#">LEARN MORE</a>
</section>

<!-- FEATURED TOURNAMENT -->
<div class="featured-bg"></div>
<h2 class="sec-title" style="top:2002px">FEATURED <b>TOURNAMENT</b></h2>
<div class="rule" style="left:545px;top:2055px;width:96px"></div>

<div class="t-card" style="left:121px"><h3>TOURNAMENT TITLE</h3><p>Lorem ipsum dolor sit amet<br>consectetur adipiscing</p><a class="btn" href="#">Learn More</a></div>
<div class="t-card" style="left:445px"><h3>TOURNAMENT TITLE</h3><p>Lorem ipsum dolor sit amet<br>consectetur adipiscing</p><a class="btn" href="#">Learn More</a></div>
<div class="t-card" style="left:758px"><h3>TOURNAMENT TITLE</h3><p>Lorem ipsum dolor sit amet<br>consectetur adipiscing</p><a class="btn" href="#">Learn More</a></div>

<div class="t-photo" style="left:151px;top:2087px;background:radial-gradient(circle at 50% 40%,#a8353a 0%,#3a2430 40%,#101722 80%)" role="img" aria-label="Player in red jersey skating with stick"></div>
<div class="t-photo" style="left:475px;top:2087px;background:radial-gradient(circle at 50% 30%,#f1f5fa 0%,#8fa7c4 40%,#2a3a55 85%)" role="img" aria-label="Group of players racing for the puck"></div>
<div class="t-photo" style="left:789px;top:2087px;background:radial-gradient(circle at 50% 60%,#d9e2ea 0%,#7c8796 40%,#1e2735 85%)" role="img" aria-label="Two players at a face-off"></div>

<!-- SUMMER -->
<section class="summer">
  <div class="summer-photo" role="img" aria-label="Player in red skating hard with ice spray in an arena"></div>
  <svg class="abs" style="left:95px;top:2740px" width="540" height="370" viewBox="0 0 540 370">
    <path d="M4 90 L4 365 L388 365 L388 359 L10 359 L10 90 Z" fill="#2aaee5"/>
    <path d="M12 2 L526 2 L432 357 L12 357 Z" fill="#ffffff"/>
  </svg>
  <h2>SUMMER <b>PROGRAMS</b></h2>
  <p>Lorem ipsum dolor sit amet, consectetur<br>adipiscing elit, sed do eiusmod<br>aliqua. Ut enim ad minim veniam, quis nostrud<br>exercitation ullamco laboris nisi ut aliquip ex<br>ea commodo consequat.</p>
  <a class="btn" href="#">View Program</a>
</section>

<!-- FOOTER -->
<footer>
  <svg class="abs" style="left:0;top:3263px" width="1200" height="175" viewBox="0 0 1200 175">
    <path d="M130 0 L1200 0 L1200 175 L0 175 L0 27 L104 27 Z" fill="#0a44a3"/>
  </svg>
  <div class="brand" style="left:120px;top:3328px;font-size:20px"><span class="dot"></span>BRAVERIDGE</div>
  <nav class="footer-links">
    <a href="#" style="left:311px">HOME</a>
    <a href="#" style="left:408px">SPRING PROGRAM</a>
    <a href="#" style="left:583px">SUMMER PROGRAM</a>
    <a href="#" style="left:765px">WINTER</a>
    <a href="#" style="left:880px">TOURNAMENT</a>
  </nav>
  <p class="copyright">© 2022 Company Name | All Rights Reserved</p>
  <div class="social"><span style="left:1012px"></span><span style="left:1040px"></span><span style="left:1067px"></span><span style="left:1095px"></span></div>
</footer>

</body>
</html>
```